The Pixel Tavern Business card.

A Simple card with our Logo and contact information. To give to investors and other professionals.

We are a nerd themed bar.
our target market is young professionals age 21+ but the real purpose of this business card is to present to potential investors and other professionals with our contact information. as we are still looking for funding before we start up.

I am partial to green and my partner likes red we are open to iteration.

Target Market(s)

Investors

Industry/Entity Type

Business

Contact Information for Business Card

Marcus Henley (555) 730-6621 kent.w4100@mailbox-demo.net Brian Tolle (555) 918-2047 briant731@mailbox-demo.net

Font styles to use
Serif

Requirements
Nice to have
• Keep it simple but not boring.
• Use the Logos but feel free to edit them to match theme/colors.
• Keep the back clean and use one of the Logos.

```html
<!DOCTYPE html>
<html lang="en">
<head>
<meta charset="utf-8">
<title>The Pixel Tavern – Business Card</title>
<link rel="stylesheet" href="https://fonts.googleapis.com/css2?family=Source+Sans+3:wght@400;700;900&display=swap">
<style>
  :root {
    --bg: #d9d9d6;
    --card: #eef0ef;
    --ink: #161616;
    --red: #e3161f;
    --grey: #4a4a4a;
    --rule: #b9bcbc;
  }
  * { box-sizing: border-box; margin: 0; padding: 0; }
  html, body { width: 1200px; height: 1120px; overflow: hidden; }
  body {
    background: var(--bg);
    font-family: "Source Sans 3", Arial, sans-serif;
    color: var(--ink);
    position: relative;
  }
  .card {
    position: absolute;
    left: 150px;
    width: 900px;
    height: 514px;
    background: var(--card);
    box-shadow: 0 6px 18px rgba(0,0,0,.18);
    overflow: hidden;
  }
  .card--front { top: 30px; }
  .card--back { top: 576px; }

  .brand {
    position: absolute;
    left: 0; right: 0;
    display: flex;
    align-items: center;
    justify-content: center;
    gap: 18px;
    font-weight: 900;
    text-transform: uppercase;
    color: var(--ink);
    letter-spacing: 1px;
  }
  .card--front .brand { top: 215px; font-size: 66px; }
  .brand__dot {
    width: 40px; height: 40px;
    border-radius: 50%;
    background: var(--red);
    flex: none;
  }
  .card--back .brand {
    top: 80px;
    font-size: 60px;
    line-height: 1;
    flex-direction: column;
    gap: 6px;
  }

  .contacts {
    position: absolute;
    top: 268px;
    left: 0; right: 0;
    display: flex;
    justify-content: center;
  }
  .contact { width: 330px; }
  .contact--left { text-align: right; padding-right: 22px; padding-top: 30px; }
  .contact--right { text-align: left; padding-left: 22px; border-left: 1px solid var(--rule); }
  .contact__name {
    color: var(--red);
    font-weight: 700;
    font-size: 30px;
    text-transform: uppercase;
    line-height: 1.2;
    margin-bottom: 8px;
  }
  .contact__line {
    font-size: 21px;
    color: var(--grey);
    line-height: 1.65;
    display: flex;
    align-items: center;
    gap: 8px;
    white-space: nowrap;
  }
  .contact--left .contact__line { justify-content: flex-end; }
  .icon { width: 18px; height: 18px; flex: none; fill: var(--grey); }

  .bands { position: absolute; left: 0; bottom: 0; width: 900px; height: 60px; }
</style>
</head>
<body>

<section class="card card--front" aria-label="Card front">
  <div class="brand"><span class="brand__dot"></span><span>The Pixel Tavern</span></div>
</section>

<section class="card card--back" aria-label="Card back">
  <div class="brand"><span>The Pixel</span><span>Tavern</span></div>

  <div class="contacts">
    <div class="contact contact--left">
      <p class="contact__name">Marcus Henley</p>
      <p class="contact__line">
        <svg class="icon" viewBox="0 0 20 20"><circle cx="10" cy="10" r="9" fill="none" stroke="#4a4a4a" stroke-width="1.6"/><path d="M7 5.5l2 2-1.2 1.4c.6 1.3 1.6 2.3 2.9 2.9l1.4-1.2 2 2-1.5 1.6C9 14 6 11 5.6 7z"/></svg>
        (555) 730-6621
      </p>
      <p class="contact__line">
        <svg class="icon" viewBox="0 0 20 20"><path d="M2 8l8-5 8 5v9H2z"/><path d="M3 8.5l7 4.5 7-4.5" fill="none" stroke="#eef0ef" stroke-width="1.4"/></svg>
        kent.w4100@mailbox-demo.net
      </p>
    </div>
    <div class="contact contact--right">
      <p class="contact__name">Brian Tolle</p>
      <p class="contact__line">
        <svg class="icon" viewBox="0 0 20 20"><circle cx="10" cy="10" r="9" fill="none" stroke="#4a4a4a" stroke-width="1.6"/><path d="M7 5.5l2 2-1.2 1.4c.6 1.3 1.6 2.3 2.9 2.9l1.4-1.2 2 2-1.5 1.6C9 14 6 11 5.6 7z"/></svg>
        (555) 918-2047
      </p>
      <p class="contact__line">
        <svg class="icon" viewBox="0 0 20 20"><path d="M2 8l8-5 8 5v9H2z"/><path d="M3 8.5l7 4.5 7-4.5" fill="none" stroke="#eef0ef" stroke-width="1.4"/></svg>
        briant731@mailbox-demo.net
      </p>
    </div>
  </div>

  <svg class="bands" viewBox="0 0 900 60" aria-hidden="true">
    <polygon points="0,40 400,36 382,60 0,60" fill="#161616"/>
    <polygon points="392,60 418,30 900,8 900,28 430,60" fill="#e3161f"/>
  </svg>
</section>

</body>
</html>
```